Gentle Willow Pregnancy and Baby Massage

I need a web design for a new business, GENTLE WILLOW PREGNANCY AND BABY MASSAGE that I am in the process of setting up in the suburbs of Perth, Western Australia. The business is owned and operated by myself and my intention is to service Pregnant Mothers and Parents of Young Babies that would benefit from massage. I would like to have a "Home Page" and pages for "About Me", "Pregnancy Massage", "Baby Massage", a Pricing Page for Pregnancy Massage Sessions, a Pricing Page for Baby Massage Sessions, and a "Contact Me" page to allow clients to either contact me with queries or book available pregnancy massage sessions on a particular day of the week. I would also like a "News" page that would include articles I have written, news about new courses and a link to my Chatterlane page (yet to be set up). I would like to keep the colour schemes similar to my logo design colours. I need the design to be easy to follow and to appeal to a younger audience (20's to mid 30's).
The target audience is pregnant mothers-to-be wishing to receive massage treatments, and new parents and grandparents of small babies that would like to learn how to massage their babies.
The look and feel should be modern, professional, elegant and feminine.
I need the design to be in a standard format such that I can update the content by myself ( and does not need specialised software) as the company and business progresses.

Target Market(s)

Industry/Entity Type

Health And Wellness

Contact Information for Business Card

Card should have rounded edges. Design should have the same "feel" as the website. Contact Details of my business address, mobile phone, email and website should be included.

Coding

Coded - Design and coding required

Number of Pages Required

5+ page

Font styles to use
Script

Requirements
Must have
• Same colours as logo design. In cmyk system, the colours are: 20,60,0,0 which best result is tintora 681 and 40,40,0,0 which best result is tintora 2645. Card should include the logo design.

```html
<!DOCTYPE html>
<html lang="en">
<head>
<meta charset="utf-8">
<title>Gentle Willow Pregnancy and Baby Massage – Benefits of Baby Massage</title>
<link href="https://fonts.googleapis.com/css2?family=Sacramento&family=Crimson+Text&family=Lato&display=swap" rel="stylesheet">
<style>
  :root {
    --backdrop: #0d0d0d;
    --page: #efe4e4;
    --teal: #94bbb8;
    --pink: #d24f9a;
    --lilac: #9a84d0;
    --quote: #6a55a8;
    --ink: #2b2326;
    --photo-light: #f7efee;
    --photo-skin: #f0c9be;
  }
  * { box-sizing: border-box; margin: 0; padding: 0; }
  html, body { width: 1200px; height: 1025px; overflow: hidden; background: var(--backdrop); }
  .page {
    position: absolute; left: 391px; top: 0; width: 418px; height: 1025px;
    background: var(--page); font-family: "Crimson Text", serif; color: var(--ink);
  }
  .site-header {
    position: absolute; left: 6px; top: 32px; width: 403px; height: 46px;
    background: var(--teal); display: flex; align-items: center; justify-content: space-between; padding: 0 12px 0 13px;
  }
  .brand { display: flex; flex-direction: column; align-items: center; color: var(--pink); font-family: "Sacramento", cursive; line-height: 1; }
  .brand-mark { width: 9px; height: 9px; border-radius: 50%; background: var(--pink); margin-bottom: 1px; }
  .brand-name { font-size: 15px; }
  .brand-tag { font-size: 8px; }
  .breadcrumb {
    position: absolute; left: 31px; top: 93px; height: 16px; padding: 0 5px;
    background: var(--teal); color: var(--pink); font-family: "Sacramento", cursive; font-size: 11px; line-height: 16px;
  }
  .hero {
    position: absolute; left: 8px; top: 122px; width: 402px; height: 220px;
    background: radial-gradient(ellipse at 60% 55%, var(--photo-skin) 0%, #f5ddd6 45%, var(--photo-light) 80%);
  }
  .section-title {
    position: absolute; left: 0; width: 418px; text-align: center;
    font-family: "Sacramento", cursive; color: var(--lilac); font-size: 27px; line-height: 30px;
  }
  .about-title { top: 347px; }
  .benefits-title { top: 705px; }
  .about-text { position: absolute; left: 21px; top: 381px; width: 222px; font-size: 10px; line-height: 12.1px; }
  .quote-card {
    position: absolute; left: 246px; top: 387px; width: 150px; height: 292px; border-radius: 3px;
    background: radial-gradient(ellipse at 60% 45%, #f1d3cc 0%, #f3e1de 55%, #f4eaea 100%);
    display: flex; flex-direction: column; justify-content: center; align-items: center; text-align: center;
    font-family: "Lato", sans-serif; color: var(--quote);
  }
  .quote-card p { font-size: 8.3px; line-height: 24px; }
  .quote-card cite { font-style: normal; font-size: 3.6px; margin-top: 3px; color: var(--ink); }
  .benefits-list { position: absolute; left: 26px; top: 754px; list-style: none; font-size: 9.4px; line-height: 11.4px; }
  .benefits-list li::before { content: "•"; display: inline-block; width: 9px; }
  .source { position: absolute; right: 24px; top: 923px; font-size: 6px; }
  .site-footer {
    position: absolute; left: 6px; top: 964px; width: 403px; height: 46px; background: var(--teal);
    display: flex; justify-content: space-around; align-items: center;
    color: var(--pink); font-family: "Crimson Text", serif; font-size: 10px;
  }
</style>
</head>
<body>
<div class="page">
  <header class="site-header">
    <svg width="26" height="20" viewBox="0 0 26 20" aria-label="Menu">
      <rect x="0" y="0" width="26" height="4.5" rx="2.2" fill="#d24f9a"/>
      <rect x="0" y="7.7" width="26" height="4.5" rx="2.2" fill="#d24f9a"/>
      <rect x="0" y="15.5" width="26" height="4.5" rx="2.2" fill="#d24f9a"/>
    </svg>
    <div class="brand">
      <span class="brand-mark"></span>
      <span class="brand-name">Gentle Willow</span>
      <span class="brand-tag">Pregnancy and Baby Massage</span>
    </div>
    <svg width="27" height="26" viewBox="0 0 27 26" aria-label="Search">
      <circle cx="10" cy="10" r="8" fill="none" stroke="#d24f9a" stroke-width="2.4"/>
      <line x1="16" y1="16" x2="25" y2="24" stroke="#d24f9a" stroke-width="3.4" stroke-linecap="round"/>
    </svg>
  </header>

  <div class="breadcrumb">Home &lt; Benefits of baby massage</div>

  <div class="hero" role="img" aria-label="Photo of a parent's hands gently holding a baby's feet"></div>

  <h1 class="section-title about-title">About Baby Massage</h1>
  <div class="about-text">
    <p>&nbsp;Baby massage was first described in China circa 4000 years ago, then in India and Egypt, and was passed down from mother to daughter over the generations. It has become more popular in the Western world over the last 20 to 30 years. Massage can start from birth and is a wonderful way to soothe, calm and enjoy time with your baby, as well as helping with the bonding process.</p>
    <p>Long before babies are able to talk, they &nbsp;communicate with the new world around them through touch. Skin sensitivity is one of the earliest functions of the body. In fact, &nbsp;stimulation of the skin is essential for adequate organic and psychological development.</p>
    <p>Whilst it is possible to learn the principles of baby massage from books, DVD's, and social media, there is really no substitute for learning from an experienced and qualified instructor. During &nbsp;classes, you will be guided through the basic strokes of Baby massage in a clear and relaxing manner. You will also learn to recognise and understand your baby's cues, which is a very important part of baby massage.</p>
  </div>

  <figure class="quote-card" role="img" aria-label="Soft photo of a baby's feet behind a quotation">
    <p>"Being touched and caressed,<br>being massaged,<br>is food for the infant.<br>Food as necessary<br>as minerals, vitamins, and proteins."</p>
    <cite>(Dr Frederic Lanoir - Noted Obstetrician and Author)</cite>
  </figure>

  <h2 class="section-title benefits-title">Benefits of Baby massage</h2>
  <ul class="benefits-list">
    <li>Relaxation of skeletal muscles</li>
    <li>Strengthens the immune system</li>
    <li>Reduces stress hormone levels in children and parents</li>
    <li>Improves sleep and regulates sleep patterns</li>
    <li>Relieves discomfort of wind, constipation, colic and reflux; sinus and chest congestion</li>
    <li>Reduces crying</li>
    <li>Enhances attachment and bonding</li>
    <li>Reduces symptoms of eczema</li>
    <li>Enhances emotions and improves mood</li>
    <li>Improves digestive, respiratory and circulatory system</li>
    <li>Reduces postnatal depression</li>
    <li>Reduces anxiety</li>
    <li>Increases blood and lymphatic circulation</li>
    <li>Enhances cognitive and motor development</li>
  </ul>
  <p class="source">Source: NIMA (Nurture Infant Massage Alliance)</p>

  <footer class="site-footer">
    <span>Chatterlane</span>
    <span>Pinwell</span>
    <span>Chirpline</span>
    <span>Orbly</span>
    <span>Snapframe</span>
  </footer>
</div>
</body>
</html>
```